Simple and clean webdesign for personal homepage

Trying to create a simple and clean webdesign for my personal homepage. Going to use a static site builder with templates to build the site. I want it to have multiple pages - like an about me, blog and resume. I just need something very basic I can customize. I want the main colors to be purple, black and white. I am open to other color palettes too but since purple is my favorite color I want that to be one of the main colors.

The site be mostly text driven. Might have some images in the body text but I want the site design to be light and lean.

Industry/Entity Type

Personal Homepage.

Coding

Coded - Design and coding required

Number of Pages Required

1 page

Font styles to use
Sans Serif

Colors
6B429C
8869AF
B7A5CE
E3DAEB
F3F0F8

Requirements
Must have
• Clean design. Purple used as a color. HTML template.
Nice to have
• Responsive

```html
<!DOCTYPE html>
<html lang="en">
<head>
<meta charset="utf-8">
<title>Daniel Carter — Web Designer</title>
<link href="https://fonts.googleapis.com/css2?family=Barlow:wght@400;500;600;700&family=Barlow+Condensed:wght@500;600&family=Rubik:wght@400;500&display=swap" rel="stylesheet">
<style>
:root{
  --purple:#6B429C;
  --purple-mid:#8869AF;
  --purple-soft:#B7A5CE;
  --purple-pale:#E3DAEB;
  --purple-mist:#F3F0F8;
  --ink:#1c1c1c;
  --text:#555;
  --muted:#888;
  --section-grey:#f4f6f9;
  --white:#fff;
  --line:#e5e5e5;
}
*{box-sizing:border-box;margin:0;padding:0}
html,body{width:1200px;height:4762px;overflow:hidden}
body{font-family:'Barlow',sans-serif;color:var(--ink);background:var(--white);position:relative}
section,header,footer{position:absolute;left:0;width:1200px}
.abs{position:absolute}
.btn{position:absolute;background:var(--purple);color:var(--white);font-size:13px;font-weight:600;display:flex;align-items:center;justify-content:center;gap:6px}
.section-title{position:absolute;left:0;width:1200px;text-align:center;color:var(--purple);font-size:32px;font-weight:600}

/* header */
.site-header{top:0;height:96px;background:var(--white)}
.brand{left:163px;top:18px;color:var(--purple);font-size:20px;font-weight:600;letter-spacing:1px;display:flex;align-items:center;gap:10px}
.brand-mark{width:14px;height:14px;border-radius:50%;background:var(--purple)}
.nav{position:absolute;top:36px;font-size:12px;font-weight:500;color:#333}
.nav.active{color:var(--purple);font-weight:600}
.nav-underline{left:533px;top:92px;width:44px;height:4px;background:var(--purple)}

/* hero */
.hero{top:96px;height:274px;background:linear-gradient(180deg,#2a2d3c 0%,#3c3f52 50%,#23252f 100%)}
.hero h1{position:absolute;top:50px;width:100%;text-align:center;color:var(--white);font-weight:400;font-size:42px}
.hero p{position:absolute;top:112px;left:240px;width:720px;text-align:center;color:#e8e8ee;font-size:13px;line-height:26px}
.hero .btn{left:510px;top:180px;width:180px;height:42px}

/* about */
.about{top:370px;height:616px}
.about .section-title{top:74px}
.intro{left:163px;top:147px;font-size:20px;font-weight:600}
.intro span{color:var(--purple)}
.bio{left:163px;width:510px;font-size:12.5px;line-height:24px;color:var(--text)}
.facts{left:790px;width:240px;font-size:12px;color:#444}
.facts b{font-weight:600;color:var(--ink)}
.fact{position:absolute;left:0;width:240px;border-bottom:1px solid var(--line);line-height:26px}
.about .btn{left:790px;top:342px;width:150px;height:37px}
.stat{position:absolute;top:440px;width:224px;text-align:center}
.stat strong{display:block;font-size:46px;font-weight:500;line-height:54px}
.stat span{font-size:17px;color:#333}
.stat-divider{top:444px;width:1px;height:108px;background:var(--line)}

/* resume */
.resume{top:986px;height:789px;background:var(--section-grey)}
.resume .section-title{top:80px}
.resume-card{position:absolute;top:155px;width:431px;height:551px;background:var(--white)}
.resume-card h3{position:absolute;left:24px;top:22px;font-family:'Barlow Condensed',sans-serif;color:var(--purple);font-size:30px;font-weight:600}
.timeline{position:absolute;left:27px;top:92px;width:1px;height:410px;background:var(--line)}
.entry{position:absolute;left:24px;width:385px}
.entry .dot{position:absolute;left:0;top:7px;width:8px;height:8px;border-radius:50%;background:var(--purple)}
.entry h4{margin-left:24px;font-family:'Barlow Condensed',sans-serif;font-weight:500;font-size:20px;color:var(--ink)}
.entry time{display:block;margin:12px 0 0 24px;font-size:11px;color:#444}
.entry p{margin:18px 0 0 24px;font-size:11px;line-height:21px;color:#444}

/* work */
.work{top:1775px;height:736px}
.work .section-title{top:76px}
.tile{position:absolute;width:204px;height:204px}
.work .btn{left:540px;top:621px;width:120px;height:43px}

/* skills */
.skills{top:2511px;height:425px;background:var(--section-grey)}
.skills .section-title{top:76px}
.skill-dot{position:absolute;width:10px;height:10px;border-radius:50%;border:2px solid var(--purple);background:var(--white)}
.skill{position:absolute;width:104px;background:var(--white);box-shadow:0 3px 10px rgba(0,0,0,.08);font-size:13px;text-align:center;color:#333;display:flex;align-items:center;justify-content:center;line-height:16px}
.skills .btn{left:540px;top:312px;width:120px;height:38px}

/* call to action */
.cta{top:2936px;height:437px;background:linear-gradient(135deg,#4a4d5a 0%,#2b2d36 55%,#3a3c47 100%)}
.cta h2{position:absolute;top:154px;width:100%;text-align:center;color:var(--white);font-size:46px;font-weight:600}
.cta .btn{left:540px;top:235px;width:120px;height:41px}

/* blog */
.blog{top:3373px;height:640px}
.blog .section-title{top:70px}
.post{position:absolute;background:var(--white);box-shadow:0 4px 16px rgba(0,0,0,.09)}
.post h3{font-family:'Rubik',sans-serif;font-weight:400;color:var(--ink)}
.post p{font-size:11px;line-height:21px;color:#333}
.post-meta{position:absolute;font-size:10px;color:var(--muted)}

/* contact */
.contact-card{top:4034px;left:233px;width:732px;height:507px;background:var(--white);box-shadow:0 4px 20px rgba(0,0,0,.08);z-index:2}
.contact-card h2{position:absolute;top:70px;width:100%;text-align:center;color:var(--purple);font-size:32px;font-weight:600}
.contact-card .lead{position:absolute;top:104px;left:70px;width:592px;text-align:center;font-size:12.5px;line-height:26px;color:#444}
.field{position:absolute;border:1px solid #ddd;font-size:11px;color:#333;padding:14px 0 0 15px}
.contact-card .btn{left:307px;top:411px;width:120px;height:42px}
.fold{position:absolute;right:0;bottom:0;width:36px;height:36px;background:linear-gradient(135deg,var(--white) 50%,var(--purple-soft) 50%)}

/* footer */
.site-footer{top:4471px;height:291px;background:#6C45A1;color:var(--white)}
.info{position:absolute;top:136px;display:flex;gap:14px;font-size:13px;line-height:24px}
.info b{font-weight:600;font-size:14px}
.footer-rule{left:163px;top:235px;width:874px;height:1px;background:rgba(255,255,255,.3)}
.copyright{left:163px;top:254px;font-size:12px}
.social{position:absolute;top:254px;width:24px;height:24px;border-radius:50%;border:1.5px solid var(--white)}
</style>
</head>
<body>

<header class="site-header">
  <div class="abs brand"><span class="brand-mark"></span>Daniel Carter</div>
  <span class="nav active" style="left:538px">HOME</span>
  <span class="nav" style="left:631px">ABOUT ME</span>
  <span class="nav" style="left:753px">BLOG</span>
  <span class="nav" style="left:841px">RESUME</span>
  <span class="nav" style="left:952px">CONTACT ME</span>
  <div class="abs nav-underline"></div>
</header>

<section class="hero" role="img" aria-label="Dark city skyline photograph behind the headline">
  <h1>I Am Web Designer</h1>
  <p>Lorem ipsum dolor sit amet, consectetuer adipiscing elit, sed diam nonummy nibh euismod tincidunt ut laoreet dolore magna aliquam erat volutpat. Ut wisi enim ad minim.</p>
  <div class="btn">
    <svg width="11" height="13" viewBox="0 0 11 13"><path d="M1 1h6l3 3v8H1z" fill="none" stroke="#fff" stroke-width="1.2"/></svg>
    Download Resume
  </div>
</section>

<section class="about">
  <h2 class="section-title">About Me</h2>
  <div class="abs intro">I'm <span>Daniel Carter,</span> a Lorem Ipsum</div>
  <p class="abs bio" style="top:186px">Donec posuere dui non auctor auctor. Ut sit amet porttitor sem. Nunc rutrum eros velrty diam posuere, sed blandit sapien tincidunt. Nulla facilisi. Praesent nisi lectus, imperdiet ac tempor ut, varius porta est. Fusce congue augue a dui ultrices luctus eget eget exhgj aenean luctus ex purus, accumsan faucibus sapien convallis eu.</p>
  <p class="abs bio" style="top:290px">Integer nisi ipsum, dictum et blandit ac, iaculis porttitor lorem. Interdum et malesuadare fames ac ante ipsum primis in faucibus. Duis sit amet arcu nec leo venenatis porttitor at id urna. Ut eros metus, sollicitudin sed dui a, consectetur egestas nisi. Maecenas mollis lorem purus, vel vehicula risus porttitor nec.</p>
  <div class="abs facts">
    <div class="fact" style="top:174px;height:36px"><b>Name:</b> Daniel Carter</div>
    <div class="fact" style="top:220px;height:36px"><b>Email:</b> info@danielcarter.net</div>
    <div class="fact" style="top:268px;height:60px;border:none"><b>Address:</b> 123 Building Name, street Name, City Name, Country - 12345</div>
  </div>
  <div class="btn">View My Full CV</div>

  <div class="stat" style="left:151px"><strong>10+</strong><span>Years Experiance</span></div>
  <div class="abs stat-divider" style="left:375px"></div>
  <div class="stat" style="left:375px"><strong>219+</strong><span>Happy Clients</span></div>
  <div class="abs stat-divider" style="left:599px"></div>
  <div class="stat" style="left:600px"><strong>540+</strong><span>Projects Done</span></div>
  <div class="abs stat-divider" style="left:823px"></div>
  <div class="stat" style="left:824px"><strong>28</strong><span>Get Awards</span></div>
</section>

<section class="resume">
  <h2 class="section-title">A Summary of My Resume</h2>

  <div class="resume-card" style="left:161px">
    <h3>My Expericence</h3>
    <div class="timeline"></div>
    <div class="entry" style="top:82px"><span class="dot"></span><h4>Senior Web Developer - Northwind Labs</h4><time>2018 - Present</time><p>Lorem ipsum dolor sit amet consectetur adipisicing elit. Velit praesentium aut repellendus rem non repudiandae sint dolor illo officia dignissimos.</p></div>
    <div class="entry" style="top:237px"><span class="dot"></span><h4>Mid-Level Web Developer - Northwind Labs</h4><time>2016 - 2018</time><p>Lorem ipsum dolor sit amet consectetur adipisicing elit. Velit praesentium aut repellendus rem non repudiandae sint dolor illo officia dignissimos.</p></div>
    <div class="entry" style="top:392px"><span class="dot"></span><h4>Junoir Web Developer - Northwind Labs</h4><time>2015 - 2016</time><p>Lorem ipsum dolor sit amet consectetur adipisicing elit. Velit praesentium aut repellendus rem non repudiandae sint dolor illo officia dignissimos.</p></div>
  </div>

  <div class="resume-card" style="left:608px">
    <h3>My Education</h3>
    <div class="entry" style="top:82px"><span class="dot"></span><h4>Enginering Degree - Lakeside University</h4><time>2015 - 2016</time><p>Lorem ipsum dolor sit amet consectetur adipisicing elit. Velit praesentium aut repellendus rem non repudiandae sint dolor illo officia dignissimos.</p></div>
    <div class="entry" style="top:237px"><span class="dot"></span><h4>Master Degree - Lakeside University</h4><time>2016 - 2018</time><p>Lorem ipsum dolor sit amet consectetur adipisicing elit. Velit praesentium aut repellendus rem non repudiandae sint dolor illo officia dignissimos.</p></div>
    <div class="entry" style="top:392px"><span class="dot"></span><h4>Bachlor Degree - Lakeside University</h4><time>2015 - 2016</time><p>Lorem ipsum dolor sit amet consectetur adipisicing elit. Velit praesentium aut repellendus rem non repudiandae sint dolor illo officia dignissimos.</p></div>
  </div>
</section>

<section class="work">
  <h2 class="section-title">My Latest Work</h2>
  <div class="tile" style="left:48px;top:155px;background:linear-gradient(135deg,#f9cf2a,#f2b705)" role="img" aria-label="Under construction website mockup on yellow"></div>
  <div class="tile" style="left:272px;top:155px;background:linear-gradient(135deg,#ececec,#d6d6d6)" role="img" aria-label="Digital marketing website mockup on grey"></div>
  <div class="tile" style="left:497px;top:155px;background:linear-gradient(135deg,#fbb55c,#f48f3c)" role="img" aria-label="Online shopping website mockup on orange"></div>
  <div class="tile" style="left:48px;top:381px;background:linear-gradient(135deg,#8fe0c8,#56c7a8)" role="img" aria-label="Pharmacy website mockup on mint"></div>
  <div class="tile" style="left:272px;top:381px;background:linear-gradient(135deg,#e6e6e6,#c9c9c9)" role="img" aria-label="Cryptocurrency landing page mockup on grey"></div>
  <div class="tile" style="left:497px;top:381px;background:linear-gradient(135deg,#f5f5f5,#e8e8e8)" role="img" aria-label="Saving money website mockup on light grey"></div>
  <div class="tile" style="left:723px;top:155px;width:429px;height:430px;background:linear-gradient(135deg,#3fe7f0,#1bd2e0)" role="img" aria-label="Startup business website mockup on cyan">
    <div class="abs" style="left:16px;top:77px;width:398px;height:260px;border-radius:12px;background:linear-gradient(135deg,#5b1a8f,#b02396 60%,#6e1c8f)"></div>
  </div>
  <div class="btn">Contact Me</div>
</section>

<section class="skills">
  <h2 class="section-title">My Skills</h2>
  <svg class="abs" style="left:110px;top:140px" width="980" height="80" viewBox="0 0 980 80">
    <path d="M0 26 Q50 14 104 24 T256 44 T410 54 T563 20 T716 26 T870 42 T980 34" fill="none" stroke="#cfcfd6" stroke-width="1" stroke-dasharray="3 3"/>
  </svg>
  <span class="skill-dot" style="left:209px;top:154px"></span>
  <span class="skill-dot" style="left:361px;top:169px"></span>
  <span class="skill-dot" style="left:515px;top:184px"></span>
  <span class="skill-dot" style="left:668px;top:145px"></span>
  <span class="skill-dot" style="left:821px;top:150px"></span>
  <span class="skill-dot" style="left:975px;top:171px"></span>
  <div class="skill" style="left:162px;top:189px;height:46px">Nunc Lacus</div>
  <div class="skill" style="left:315px;top:206px;height:52px">Fermentum<br>Dolor</div>
  <div class="skill" style="left:468px;top:220px;height:52px">Vestibulum<br>Ante</div>
  <div class="skill" style="left:621px;top:180px;height:46px">Enim Vitae</div>
  <div class="skill" style="left:774px;top:184px;height:52px">Iaculis<br>Porttitor</div>
  <div class="skill" style="left:928px;top:206px;height:52px">Suspendisse<br>Velit</div>
  <div class="btn">Contact Me</div>
</section>

<section class="cta" role="img" aria-label="Dim photograph of a laptop on a desk">
  <h2>Interested In Working With Me?</h2>
  <div class="btn">Hire Me!</div>
</section>

<section class="blog">
  <h2 class="section-title">My Blog</h2>
  <article class="post" style="left:161px;top:147px;width:445px;height:420px">
    <div style="height:202px;background:linear-gradient(135deg,#2b5fa8,#1e4f94 60%,#e7b43a)" role="img" aria-label="Man at a desk in front of a chalkboard wall"></div>
    <h3 style="position:absolute;left:22px;top:222px;width:400px;font-size:20px;line-height:29px">Lorem Ipsum Dolor Sit Amet Consectetuer Adipiscing</h3>
    <p style="position:absolute;left:22px;top:290px;width:405px">sed diam nonummy nibh euismod tincid unt ut laoreet dolore magna aliqua erat volutpat nonummy nibh. sed diam nonummy nibh euismod tincid unt ut laoreet dolore magna sed diam nonummy nibh euismod tincid unt.</p>
    <span class="post-meta" style="left:22px;top:384px">By Sam Rivers</span>
    <span class="post-meta" style="right:22px;top:384px">• 04 month ago</span>
  </article>
  <article class="post" style="left:630px;top:147px;width:407px;height:200px">
    <div class="abs" style="left:0;top:0;width:174px;height:200px;background:linear-gradient(135deg,#f3e6d4,#e9c99a 60%,#f4e04a)" role="img" aria-label="Child writing at a table"></div>
    <h3 style="position:absolute;left:197px;top:18px;width:190px;font-size:20px;line-height:29px">Lorem Ipsum Dolor Amet Consectet</h3>
    <p style="position:absolute;left:197px;top:84px;width:190px">sed diam nonummy nibh euismod tincid unt ut laoreet dolore magna aliquam erat volutpat nonummy nibh.</p>
  </article>
  <article class="post" style="left:630px;top:369px;width:407px;height:198px">
    <div class="abs" style="left:0;top:0;width:174px;height:198px;background:linear-gradient(135deg,#c9a787,#b8926f)" role="img" aria-label="Pins forming numerals on a corkboard"></div>
    <h3 style="position:absolute;left:197px;top:18px;width:190px;font-size:20px;line-height:29px">Lorem Ipsum Dolor Amet Consectet</h3>
    <p style="position:absolute;left:197px;top:84px;width:190px">sed diam nonummy nibh euismod tincid unt ut laoreet dolore magna aliquam erat volutpat nonummy nibhnibh.</p>
  </article>
</section>

<section class="contact-card">
  <h2>Contact Me</h2>
  <p class="lead">Etiam id commodo nisi vel accumsan quam quisque vehicula velit ac rhoncus facilisis augue metus maximus orciac auctor lacus nisi sed turpis cras ac lorem eu eros fringilla vestibulum.</p>
  <div class="field" style="left:67px;top:174px;width:292px;height:45px">Name</div>
  <div class="field" style="left:374px;top:174px;width:292px;height:45px">Email</div>
  <div class="field" style="left:67px;top:232px;width:292px;height:44px">Phone</div>
  <div class="field" style="left:374px;top:232px;width:292px;height:44px">Company</div>
  <div class="field" style="left:67px;top:287px;width:599px;height:91px">Message</div>
  <div class="btn">Submit Now</div>
  <div class="fold"></div>
</section>

<footer class="site-footer">
  <div class="info" style="left:200px">
    <svg width="32" height="34" viewBox="0 0 32 34"><path d="M16 3a9 9 0 0 0-9 9c0 7 9 15 9 15s9-8 9-15a9 9 0 0 0-9-9z" fill="none" stroke="#fff" stroke-width="1.5"/><circle cx="16" cy="12" r="3.5" fill="none" stroke="#fff" stroke-width="1.5"/><ellipse cx="16" cy="29" rx="12" ry="3" fill="none" stroke="#fff" stroke-width="1.2"/></svg>
    <div>123 Building Name, street Name,<br>City Name, Country - 12345</div>
  </div>
  <div class="info" style="left:532px">
    <svg width="34" height="34" viewBox="0 0 34 34"><path d="M8 4l5 6-3 3c2 5 6 9 11 11l3-3 6 5-4 4C15 29 5 19 4 8z" fill="none" stroke="#fff" stroke-width="1.5" stroke-linejoin="round"/></svg>
    <div><b>Phone</b><br>(+060) 555 010 200</div>
  </div>
  <div class="info" style="left:784px">
    <svg width="34" height="34" viewBox="0 0 34 34"><path d="M3 14l14-10 14 10v16H3z M3 14l14 10 14-10" fill="none" stroke="#fff" stroke-width="1.5" stroke-linejoin="round"/><rect x="9" y="9" width="16" height="10" fill="none" stroke="#fff" stroke-width="1.2"/></svg>
    <div><b>Email</b><br>info@danielcarter.net</div>
  </div>
  <div class="abs footer-rule"></div>
  <div class="abs copyright">Copyright © 2022 Daniel Carter. All Rights Reserved.</div>
  <span class="social" style="left:951px" aria-label="Social profile"></span>
  <span class="social" style="left:983px" aria-label="Social profile"></span>
  <span class="social" style="left:1014px" aria-label="Social profile"></span>
</footer>

</body>
</html>
```